I need three graphics made that will go on walls in a basketball lockerroom

I need three graphics made that will go on a basketball lockerroom wall. Here are the specifics.
Graphic 1 (Size 115" wide by 52" tall, min 150 DPI)
This should be something that displays the acronym for TOLVAR. The main background color should be the teal color attached. Use logos and the other approved colors as needed.
Standards
Intensity
Effort
Grit
Energy
Love
Graphic 2 (Size 88" wide by 52" tall, min 150 DPI)
This one should be on the Navy Blue background color attached
and impactful way say Attitude and Effort
Graphic 3 (Size 100" wide by 18" tall, min 150 DPI)
This goes along the top of the way and needs to say
(THS logo) Stars Lead the Way (Star logo) Tolvar Basketball (THS logo)
All three of these need to feel like they are of the same style. For Graphic #2 I thought something maybe like the attached basketball except use the S Star in the middle and say attitude and effort using the colors .. but I'm open to other ideas

```html
<!DOCTYPE html>
<html lang="en">
<head>
<meta charset="utf-8">
<title>Tolvar Basketball Locker Room Graphics</title>
<link rel="stylesheet" href="https://fonts.googleapis.com/css2?family=Graduate&family=Roboto+Condensed:wght@700&display=swap">
<style>
  :root {
    --paper: #ffffff;
    --teal-dark: #033f50;
    --teal-mid: #045a63;
    --navy-dark: #0c1a36;
    --navy-mid: #10284f;
    --banner-dark: #03222f;
    --banner-mid: #063547;
    --cyan: #00eef2;
    --player: #0d8384;
    --rule: #ffffff;
    --silver-light: #ffffff;
    --silver-mid: #d9d9d9;
    --silver-dark: #8e8e8e;
  }
  html, body {
    margin: 0;
    padding: 0;
    overflow: hidden;
    background: var(--paper);
  }
  .sheet {
    position: relative;
    width: 933px;
    height: 1200px;
    overflow: hidden;
    background: var(--paper);
  }
  .graphic {
    position: absolute;
    display: block;
  }
  .graphic--acronym { left: 53px; top: 119px; width: 800px; height: 362px; }
  .graphic--attitude { left: 147px; top: 528px; width: 612px; height: 361px; }
  .graphic--banner { left: 105px; top: 955px; width: 695px; height: 125px; }
  .big-letter, .headline, .brand-name, .banner-motto {
    font-family: "Graduate", serif;
  }
  .big-letter, .headline {
    stroke-width: 4;
    stroke-linejoin: round;
    paint-order: stroke fill;
  }
  .value-label {
    font-family: "Roboto Condensed", sans-serif;
    font-weight: 700;
    font-size: 24px;
    fill: var(--cyan);
  }
  .leader { stroke: var(--rule); stroke-width: 1; fill: none; }
  .player-area { fill: var(--player); opacity: 0.45; }
  .brand-name { fill: var(--rule); }
  .brand-mark { fill: var(--cyan); }
  .amp-ring { fill: none; stroke: var(--cyan); stroke-width: 2.5; }
  .amp { font-family: "Roboto Condensed", sans-serif; font-size: 34px; fill: var(--cyan); }
  .banner-motto { font-size: 19px; fill: var(--silver-mid); }
</style>
</head>
<body>
<main class="sheet">

  <!-- Graphic 1: acronym wall -->
  <svg class="graphic graphic--acronym" viewBox="0 0 800 362" aria-labelledby="acronym-title">
    <title id="acronym-title">TOLVAR: Standards, Intensity, Effort, Grit, Energy, Love</title>
    <defs>
      <linearGradient id="teal-bg" x1="0" y1="0" x2="1" y2="1">
        <stop offset="0" stop-color="var(--teal-dark)"/>
        <stop offset="0.5" stop-color="var(--teal-mid)"/>
        <stop offset="1" stop-color="var(--teal-dark)"/>
      </linearGradient>
      <linearGradient id="silver" x1="0" y1="0" x2="1" y2="0">
        <stop offset="0" stop-color="var(--silver-mid)"/>
        <stop offset="0.45" stop-color="var(--silver-light)"/>
        <stop offset="1" stop-color="var(--silver-dark)"/>
      </linearGradient>
    </defs>
    <rect width="800" height="362" fill="url(#teal-bg)"/>

    <g class="leaders">
      <path class="leader" d="M88 0V65M84 61l4 4 4-4"/>
      <path class="leader" d="M205 0V180M201 176l4 4 4-4"/>
      <path class="leader" d="M302 0V65M298 61l4 4 4-4"/>
      <path class="leader" d="M420 0V180M416 176l4 4 4-4"/>
      <path class="leader" d="M521 0V65M517 61l4 4 4-4"/>
      <path class="leader" d="M643 0V180M639 176l4 4 4-4"/>
    </g>

    <g class="players">
      <rect class="player-area" x="156" y="99" width="38" height="95" rx="8" role="img" aria-label="Basketball player dribbling silhouette"/>
      <rect class="player-area" x="369" y="90" width="40" height="104" rx="8" role="img" aria-label="Basketball player dunking silhouette"/>
      <rect class="player-area" x="589" y="103" width="42" height="91" rx="8" role="img" aria-label="Basketball player driving silhouette"/>
      <rect class="player-area" x="272" y="215" width="36" height="91" rx="8" role="img" aria-label="Basketball player passing silhouette"/>
      <rect class="player-area" x="487" y="188" width="28" height="118" rx="8" role="img" aria-label="Basketball player shooting silhouette"/>
      <rect class="player-area" x="707" y="196" width="46" height="120" rx="8" role="img" aria-label="Basketball player laying up silhouette"/>
    </g>

    <g class="values">
      <text class="value-label" x="88" y="87">Standards</text>
      <text class="value-label" x="205" y="202">Intensity</text>
      <text class="value-label" x="301" y="89">Effort</text>
      <text class="value-label" x="420" y="202">Grit</text>
      <text class="value-label" x="521" y="89">Energy</text>
      <text class="value-label" x="643" y="202">Love</text>
    </g>

    <g class="big-letters" fill="url(#silver)" stroke="url(#silver)">
      <text class="big-letter" x="90" y="194" font-size="130" textLength="60" lengthAdjust="spacingAndGlyphs">T</text>
      <text class="big-letter" x="206" y="306" font-size="130" textLength="60" lengthAdjust="spacingAndGlyphs">O</text>
      <text class="big-letter" x="303" y="194" font-size="130" textLength="60" lengthAdjust="spacingAndGlyphs">L</text>
      <text class="big-letter" x="421" y="306" font-size="130" textLength="60" lengthAdjust="spacingAndGlyphs">V</text>
      <text class="big-letter" x="523" y="194" font-size="130" textLength="60" lengthAdjust="spacingAndGlyphs">A</text>
      <text class="big-letter" x="644" y="306" font-size="130" textLength="58" lengthAdjust="spacingAndGlyphs">R</text>
    </g>

    <g class="brand">
      <circle class="brand-mark" cx="66" cy="266" r="9"/>
      <text class="brand-name" x="81" y="274" font-size="22">TOLVAR</text>
    </g>
  </svg>

  <!-- Graphic 2: attitude & effort -->
  <svg class="graphic graphic--attitude" viewBox="0 0 612 361" aria-labelledby="attitude-title">
    <title id="attitude-title">Attitude and Effort</title>
    <defs>
      <linearGradient id="navy-bg" x1="0" y1="0" x2="1" y2="1">
        <stop offset="0" stop-color="var(--navy-dark)"/>
        <stop offset="0.55" stop-color="var(--navy-mid)"/>
        <stop offset="1" stop-color="var(--navy-dark)"/>
      </linearGradient>
      <linearGradient id="silver-wide" x1="0" y1="0" x2="1" y2="0">
        <stop offset="0" stop-color="var(--silver-dark)"/>
        <stop offset="0.5" stop-color="var(--silver-light)"/>
        <stop offset="1" stop-color="var(--silver-mid)"/>
      </linearGradient>
    </defs>
    <rect width="612" height="361" fill="url(#navy-bg)"/>

    <rect class="player-area" x="510" y="51" width="100" height="102" rx="12" role="img" aria-label="Basketball player shooting silhouette with shadow"/>
    <rect class="player-area" x="30" y="181" width="120" height="109" rx="12" role="img" aria-label="Basketball player defending silhouette with shadow"/>

    <g class="headlines" fill="url(#silver-wide)" stroke="url(#silver-wide)">
      <text class="headline" x="111" y="143" font-size="96" textLength="391" lengthAdjust="spacingAndGlyphs">ATTITUDE</text>
      <text class="headline" x="158" y="287" font-size="96" textLength="297" lengthAdjust="spacingAndGlyphs">EFFORT</text>
    </g>

    <circle class="amp-ring" cx="306" cy="180" r="23"/>
    <text class="amp" x="306" y="192" text-anchor="middle">&amp;</text>
  </svg>

  <!-- Graphic 3: top-of-wall banner -->
  <svg class="graphic graphic--banner" viewBox="0 0 695 125" aria-labelledby="banner-title">
    <title id="banner-title">THS — Stars Lead the Way — Tolvar Basketball</title>
    <defs>
      <linearGradient id="banner-bg" x1="0" y1="0" x2="1" y2="0">
        <stop offset="0" stop-color="var(--banner-mid)"/>
        <stop offset="0.5" stop-color="var(--banner-dark)"/>
        <stop offset="1" stop-color="var(--banner-mid)"/>
      </linearGradient>
    </defs>
    <rect width="695" height="125" fill="url(#banner-bg)"/>

    <text class="brand-name" x="146" y="70" font-size="40" text-anchor="middle">THS</text>
    <text class="banner-motto" x="146" y="104" text-anchor="middle" textLength="200" lengthAdjust="spacingAndGlyphs">STARS LEAD THE WAY</text>

    <circle class="brand-mark" cx="352" cy="63" r="9"/>
    <text class="brand-name" x="367" y="71" font-size="22">TOLVAR</text>

    <circle class="brand-mark" cx="470" cy="49" r="10"/>
    <text class="brand-name" x="486" y="55" font-size="16">BRENNICK HOOPS</text>
    <text class="banner-motto" x="544" y="104" text-anchor="middle" textLength="190" lengthAdjust="spacingAndGlyphs">TOLVAR BASKETBALL</text>
  </svg>

</main>
</body>
</html>
```